Estate Agent/Real Estate valuation tool

We need a design for our our new estate agent valuation tool.

The tool allows users to book a valuation of their house/property with the estate agent, after they choose there property they can then complete their details and choose a booking time.

The mock up of the design we want is attached to this project.(Main Screen)

This also needs to be responsive so the design is easy to use on a mobile device.

Target Market(s)

estate agents

Industry/Entity Type

Real Estate Agent

Number of Pages Required

1 page

Requirements
Must have
• Section 2 and 3 greyed out when user is on step 1
• Section 1 and 3 greyed out when user is on step 2
• Section 1 and 2 greyed out when the user is on step 3
• *** Design must be shown for mobile/ipad and desktop
Nice to have
• Clean and Simple
Should not have
• Dark colours

```html
<!DOCTYPE html>
<html lang="en">
<head>
<meta charset="utf-8">
<title>Valuation Booking – Mobile</title>
<link rel="stylesheet" href="https://fonts.googleapis.com/css2?family=Alegreya+Sans:wght@800&family=Arimo:wght@700&family=Marcellus&family=Noto+Serif&display=swap">
<style>
  :root {
    --backdrop: #b3b3b3;
    --panel: #d4d4d4;
    --day-cell: #c6c6c6;
    --day-border: #777777;
    --slot: #f1f1f1;
    --slot-selected: #c9e8fb;
    --text: #111111;
    --divider: #6a6a6c;
    --accent: #3a97d9;
    --accent-light: #c8e8fb;
    --ribbon: #f00000;
    --white: #ffffff;
  }
  * { box-sizing: border-box; margin: 0; padding: 0; }
  html, body { width: 1200px; height: 900px; overflow: hidden; }
  body { position: relative; background: var(--backdrop); }

  .footer-band { position: absolute; left: 0; top: 855px; width: 1200px; height: 45px; background: var(--accent); }

  .phone-screen { position: absolute; left: 255px; top: 0; width: 710px; height: 665px; background: var(--panel); }

  .step-tabs { position: absolute; left: 40px; top: -4px; display: flex; gap: 4px; }
  .step-tab { width: 205px; height: 12px; background: var(--day-cell); border: 2px solid var(--day-border); }
  .step-tab.is-active { background: var(--accent); border-color: var(--accent); }

  .day-picker { position: absolute; left: 41px; top: 22px; display: flex; gap: 4px; }
  .day-option {
    width: 203px; height: 206px; background: var(--day-cell); border: 2px solid var(--day-border);
    display: flex; align-items: center; justify-content: center;
    font-family: "Noto Serif", serif; font-size: 40px; color: var(--text); white-space: nowrap;
  }

  .slot-list { position: absolute; left: 38px; top: 238px; }
  .slot { position: absolute; left: 0; display: flex; }
  .slot-date, .slot-time {
    height: 76px; background: var(--slot); display: flex; align-items: center;
    font-family: "Alegreya Sans", sans-serif; font-weight: 800; font-size: 35px; color: var(--text);
  }
  .slot-date { width: 485px; padding-left: 25px; }
  .slot-time { position: absolute; left: 512px; width: 110px; justify-content: center; }
  .slot.is-selected .slot-date, .slot.is-selected .slot-time { background: var(--slot-selected); }

  .divider-bar { position: absolute; left: 255px; top: 665px; width: 710px; height: 22px; background: var(--divider); }

  .confirm-button {
    position: absolute; left: 255px; top: 687px; width: 710px; height: 131px;
    background: linear-gradient(to bottom, var(--accent-light), var(--accent));
    display: flex; align-items: center; padding-left: 80px;
    font-family: "Marcellus", serif; font-size: 47px; color: var(--white); letter-spacing: 1px;
  }

  .version-ribbon { position: absolute; left: 0; top: 0; }
</style>
</head>
<body>
  <div class="phone-screen">
    <div class="step-tabs">
      <div class="step-tab is-active"></div>
      <div class="step-tab"></div>
      <div class="step-tab"></div>
    </div>

    <div class="day-picker">
      <div class="day-option">Wed 2nd</div>
      <div class="day-option">Thurs 3rd</div>
      <div class="day-option">Fri 4th</div>
    </div>

    <div class="slot-list">
      <div class="slot" style="top:0"><div class="slot-date">Sunday 29th November</div><div class="slot-time">08:10</div></div>
      <div class="slot" style="top:84px"><div class="slot-date">Sunday 29th November</div><div class="slot-time">09:20</div></div>
      <div class="slot is-selected" style="top:170px"><div class="slot-date">Sunday 29th November</div><div class="slot-time">11:20</div></div>
      <div class="slot" style="top:254px"><div class="slot-date">Sunday 29th November</div><div class="slot-time">12:30</div></div>
      <div class="slot" style="top:338px"><div class="slot-date">Sunday 29th November</div><div class="slot-time">14:10</div></div>
    </div>
  </div>

  <div class="divider-bar"></div>
  <div class="confirm-button">CONFIRM BOOKING</div>
  <div class="footer-band"></div>

  <svg class="version-ribbon" width="520" height="380" viewBox="0 0 520 380">
    <polygon points="0,215 332,0 502,40 0,365" fill="var(--ribbon)"/>
    <text x="236" y="178" transform="rotate(-33 236 160)" text-anchor="middle"
          font-family="Arimo, sans-serif" font-weight="700" font-size="58" fill="#000">Mobile version</text>
  </svg>
</body>
</html>
```